Harbin Motors LLC

Car Dealer Customer Service
Address: 2847 Calloway Avenue, Brenton Falls, TN 38999
web: www.harbinmotorsco.example
email: harbinmotorsco@mailbox.example
Phone: (931) 555-0147
Phone: (629) 555-0183

```html
<!DOCTYPE html>
<html lang="en">
<head>
<meta charset="utf-8">
<title>Harbin Motors LLC – Business Card</title>
<link rel="stylesheet" href="https://fonts.googleapis.com/css2?family=Montserrat:wght@400;500;800&display=swap">
<style>
  :root {
    --bg: #e9eaec;
    --card: #ffffff;
    --brand-blue: #1f78b4;
    --band-blue: #2a93d0;
    --accent-gold: #ebb13f;
    --ink: #1b1b1b;
  }
  * { margin: 0; padding: 0; box-sizing: border-box; }
  html, body { width: 1200px; height: 900px; overflow: hidden; }
  body {
    background: var(--bg);
    font-family: "Montserrat", sans-serif;
    position: relative;
  }
  .card {
    position: absolute;
    width: 700px;
    height: 400px;
    background: var(--card);
    box-shadow: 0 6px 18px rgba(0,0,0,0.12);
    overflow: hidden;
  }
  .card--front { left: 110px; top: 40px; }
  .card--back { left: 390px; top: 460px; }

  .brand {
    display: flex;
    align-items: center;
    gap: 16px;
  }
  .brand__dot {
    width: 54px;
    height: 54px;
    border-radius: 50%;
    background: var(--brand-blue);
    flex: none;
  }
  .brand__name {
    font-weight: 800;
    color: var(--brand-blue);
    font-size: 40px;
    letter-spacing: 1px;
    line-height: 1;
    white-space: nowrap;
  }
  .card--front .brand {
    position: absolute;
    left: 50%;
    top: 50%;
    transform: translate(-50%, -50%);
  }

  .card--back .brand {
    position: absolute;
    left: 25px;
    top: 145px;
    flex-direction: column;
    align-items: center;
    gap: 16px;
    width: 315px;
  }
  .card--back .brand__dot { width: 80px; height: 80px; }
  .card--back .brand__name { font-size: 28px; text-align: center; }

  .divider {
    position: absolute;
    left: 355px;
    top: 70px;
    width: 2px;
    height: 200px;
    background: var(--brand-blue);
  }
  .contact {
    position: absolute;
    left: 380px;
    top: 68px;
    color: var(--ink);
    font-size: 15px;
    line-height: 1.55;
  }
  .contact__role { font-weight: 500; }
  .contact__address { margin-bottom: 6px; }
  .contact__list { list-style: none; }
  .contact__list li { display: flex; align-items: center; gap: 8px; white-space: nowrap; }
  .contact__list svg { width: 14px; height: 14px; flex: none; }
  .contact__domain { color: var(--band-blue); }

  .wave { position: absolute; left: 0; top: 0; width: 700px; height: 400px; }
</style>
</head>
<body>
  <section class="card card--front" aria-label="Card front">
    <div class="brand">
      <span class="brand__dot"></span>
      <span class="brand__name">HARBIN MOTORS</span>
    </div>
  </section>

  <section class="card card--back" aria-label="Card back">
    <svg class="wave" viewBox="0 0 700 400" aria-hidden="true">
      <path d="M0 340 C 220 335 480 300 700 238 L700 400 L0 400 Z" fill="var(--band-blue)"/>
      <path d="M250 318 C 430 305 590 265 700 218" fill="none" stroke="var(--accent-gold)" stroke-width="5"/>
    </svg>

    <div class="brand">
      <span class="brand__dot"></span>
      <span class="brand__name">HARBIN MOTORS</span>
    </div>

    <span class="divider"></span>

    <div class="contact">
      <p class="contact__role">Car Dealer Customer Service</p>
      <p class="contact__address">2847 Calloway Avenue,<br>Brenton Falls, TN 38999</p>
      <ul class="contact__list">
        <li>
          <svg viewBox="0 0 16 16"><path d="M3 1h3l1.5 4-2 1.3a9 9 0 0 0 4.2 4.2L11 8.5l4 1.5v3a2 2 0 0 1-2 2A12 12 0 0 1 1 3a2 2 0 0 1 2-2z" fill="var(--band-blue)"/></svg>
          (931) 555-0147
        </li>
        <li>
          <svg viewBox="0 0 16 16"><rect x="1" y="3" width="14" height="4" rx="2" fill="var(--band-blue)"/><rect x="3" y="7" width="10" height="7" rx="1" fill="var(--band-blue)"/></svg>
          (629) 555-0183
        </li>
        <li>
          <svg viewBox="0 0 16 16"><rect x="1" y="3" width="14" height="10" fill="var(--band-blue)"/><path d="M1 3l7 6 7-6" fill="none" stroke="#fff" stroke-width="1.2"/></svg>
          harbinmotorsco@mailbox.example
        </li>
        <li>
          <svg viewBox="0 0 16 16"><circle cx="8" cy="8" r="7" fill="var(--band-blue)"/><path d="M1 8h14M8 1c-3 3-3 11 0 14M8 1c3 3 3 11 0 14" fill="none" stroke="#fff" stroke-width="0.9"/></svg>
          <span>www.<span class="contact__domain">harbinmotorsco</span>.example</span>
        </li>
      </ul>
    </div>
  </section>
</body>
</html>
```